Product label

Create a hip label for a small line of products to be sold at a barbershop.
Updates

Reason: I'm extending the dead line to have improvements made....also since you guys all over the world, I want to accomadet for the day and time differences. Thank you for understanding

Target Market(s)

Men with facial hair....

Industry/Entity Type

Product

Colors

Requirements
Nice to have
• Nostalgic look, current vibe, easy to read . will need room for ingredients list on the label along with business details...website, no animal testing, made in the USA and shop logo..I'm not apposed to having the logo as a secondary feature on the label as well. Please as creative as you want to be....

```html
<!DOCTYPE html>
<html lang="en">
<head>
<meta charset="utf-8">
<title>The Copper Blade – Product Labels</title>
<link href="https://fonts.googleapis.com/css2?family=Cinzel:wght@700&family=Montserrat:wght@400&display=swap" rel="stylesheet">
<style>
  :root {
    --bg: #ffffff;
    --ink: #ffffff;
    --amber-deep: #6a3d15;
    --amber-mid: #a2611f;
    --amber-bright: #c97e2a;
  }
  html, body { margin: 0; padding: 0; overflow: hidden; background: var(--bg); }
  .canvas { position: relative; width: 1200px; height: 1053px; overflow: hidden; background: var(--bg); }
  .label-art { position: absolute; inset: 0; }
  .brand-name, .product-title, .ingredients {
    position: absolute; transform: translateX(-50%); color: var(--ink); text-align: center; margin: 0;
  }
  .brand-name {
    font-family: "Cinzel", serif; font-weight: 700; white-space: nowrap; letter-spacing: 1px;
  }
  .brand-name--shampoo { left: 330px; top: 150px; font-size: 34px; }
  .brand-name--oil { left: 955px; top: 106px; font-size: 26px; }
  .product-title {
    font-family: "Cinzel", serif; font-weight: 700; white-space: nowrap; letter-spacing: 2px;
  }
  .product-title--shampoo { left: 333px; top: 318px; font-size: 58px; }
  .product-title--oil { left: 952px; top: 240px; font-size: 42px; }
  .ingredients {
    font-family: "Montserrat", sans-serif; text-transform: uppercase; letter-spacing: 1.6px;
  }
  .ingredients h3 { font-weight: 400; margin: 0; }
  .ingredients p { margin: 0; }
  .ingredients--shampoo { left: 337px; top: 487px; width: 440px; font-size: 13.5px; line-height: 21.5px; }
  .ingredients--shampoo h3 { font-size: 14px; margin-bottom: 12px; }
  .ingredients--oil { left: 955px; top: 364px; width: 330px; font-size: 10.5px; line-height: 17.5px; }
  .ingredients--oil h3 { font-size: 11px; margin-bottom: 6px; }
</style>
</head>
<body>
<div class="canvas">
  <svg class="label-art" width="1200" height="1053" viewBox="0 0 1200 1053" aria-hidden="true">
    <defs>
      <linearGradient id="amberShampoo" x1="0" x2="1" y1="0" y2="0">
        <stop offset="0" stop-color="var(--amber-deep)"/>
        <stop offset="0.25" stop-color="var(--amber-mid)"/>
        <stop offset="0.5" stop-color="var(--amber-bright)"/>
        <stop offset="0.75" stop-color="var(--amber-mid)"/>
        <stop offset="1" stop-color="var(--amber-deep)"/>
      </linearGradient>
      <linearGradient id="amberOil" x1="0" x2="1" y1="0" y2="0">
        <stop offset="0" stop-color="var(--amber-deep)"/>
        <stop offset="0.3" stop-color="var(--amber-bright)"/>
        <stop offset="0.7" stop-color="var(--amber-bright)"/>
        <stop offset="1" stop-color="var(--amber-deep)"/>
      </linearGradient>
    </defs>

    <!-- shampoo label -->
    <path class="label-shape" d="M0 1053 V215 Q0 0 215 0 H460 Q675 0 675 215 V1053 Z" fill="url(#amberShampoo)"/>
    <path class="label-frame" fill="none" stroke="var(--ink)" stroke-width="3"
      d="M156 197 H78 A20 20 0 0 1 58 217 V968 A20 20 0 0 1 78 988 H597 A20 20 0 0 1 617 968 V217 A20 20 0 0 1 597 197 H527"/>
    <g class="title-rules" stroke="var(--ink)">
      <line x1="132" y1="305" x2="535" y2="305" stroke-width="2" stroke-dasharray="14 3"/>
      <line x1="132" y1="313" x2="535" y2="313" stroke-width="1.5"/>
      <line x1="132" y1="397" x2="535" y2="397" stroke-width="1.5"/>
      <line x1="132" y1="405" x2="535" y2="405" stroke-width="2" stroke-dasharray="14 3"/>
      <path d="M132 352 L168 349 V355 Z M535 352 L499 349 V355 Z" fill="var(--ink)" stroke="none"/>
    </g>

    <!-- beard oil label -->
    <path class="label-shape" d="M696 1053 V150 Q696 0 846 0 H1050 Q1200 0 1200 150 V903 Q1200 1053 1050 1053 Z" fill="url(#amberOil)"/>
    <path class="label-frame" fill="none" stroke="var(--ink)" stroke-width="3"
      d="M815 140 H762 A18 18 0 0 1 744 158 V719 A18 18 0 0 1 762 737 H1142 A18 18 0 0 1 1160 719 V158 A18 18 0 0 1 1142 140 H1095"/>
    <g class="title-rules" stroke="var(--ink)">
      <line x1="798" y1="225" x2="1103" y2="225" stroke-width="2" stroke-dasharray="12 3"/>
      <line x1="798" y1="233" x2="1103" y2="233" stroke-width="1.5"/>
      <line x1="798" y1="296" x2="1103" y2="296" stroke-width="1.5"/>
      <line x1="798" y1="304" x2="1103" y2="304" stroke-width="2" stroke-dasharray="12 3"/>
      <path d="M785 264 L815 261 V267 Z M1118 264 L1088 261 V267 Z" fill="var(--ink)" stroke="none"/>
    </g>
  </svg>

  <p class="brand-name brand-name--shampoo">The Copper Blade</p>
  <h2 class="product-title product-title--shampoo">SHAMPOO</h2>
  <div class="ingredients ingredients--shampoo">
    <h3>Ingredients:</h3>
    <p>Insert information here as required, could also include product descrip&shy;tion or history/mock history of the brand.....</p>
  </div>

  <p class="brand-name brand-name--oil">The Copper Blade</p>
  <h2 class="product-title product-title--oil">BEARD OIL</h2>
  <div class="ingredients ingredients--oil">
    <h3>Ingredients:</h3>
    <p>Insert information here as required, could also include product descrip&shy;tion or history/mock history of the brand.....</p>
  </div>
</div>
</body>
</html>
```